Fitness Training academy needs a business card design

We need a business card design for a NEW business that teaches/trains people how to become personal trainers. We would like to see designs both with and without our QR code. We would like our designs double sided.

See the following attachments
Design Brief
Logos (both black background, white background in all formats)
QR Code

```html
<!DOCTYPE html>
<html lang="en">
<head>
<meta charset="utf-8">
<title>Stride Coaching Institute – Business Card</title>
<link href="https://fonts.googleapis.com/css2?family=Oswald:wght@400;500&family=Open+Sans:wght@400;600&display=swap" rel="stylesheet">
<style>
  :root {
    --bg: #e9e7e4;
    --black: #0c0c0c;
    --charcoal: #2a2a2a;
    --grey: #9a9a9a;
    --grey-light: #cfcfcf;
    --paper: #f7f7f7;
    --orange: #f7941d;
    --red-orange: #e8381b;
    --text-dark: #3a3a3a;
    --white: #ffffff;
  }
  * { margin: 0; padding: 0; box-sizing: border-box; }
  html, body { width: 1200px; height: 829px; overflow: hidden; }
  body {
    background: var(--bg);
    font-family: "Open Sans", Arial, sans-serif;
    position: relative;
  }
  .card {
    position: absolute;
    top: 266px;
    width: 520px;
    height: 297px;
    overflow: hidden;
    box-shadow: 0 6px 18px rgba(0,0,0,0.18);
  }
  .card--front { left: 50px; }
  .card--back { left: 630px; }
  .card__art { position: absolute; inset: 0; width: 100%; height: 100%; }

  .brand { position: absolute; display: flex; align-items: center; gap: 12px; }
  .brand__ring {
    width: 62px; height: 62px; border-radius: 50%;
    border: 4px solid var(--grey);
    flex: none;
  }
  .brand__text { display: flex; flex-direction: column; }
  .brand__name {
    font-family: "Oswald", Arial, sans-serif;
    font-weight: 500;
    font-size: 22px;
    letter-spacing: 0.5px;
    text-transform: uppercase;
    white-space: nowrap;
  }
  .brand__tagline {
    font-size: 7px;
    letter-spacing: 2.4px;
    text-transform: uppercase;
    color: var(--grey);
    margin-top: 1px;
  }
  .card--front .brand { left: 108px; top: 104px; }
  .card--front .brand__name { color: var(--white); }
  .card--back .brand { right: 30px; top: 46px; }
  .card--back .brand__name { color: var(--text-dark); }

  .website {
    position: absolute;
    left: 22px; bottom: 14px;
    color: var(--white);
    font-size: 12px;
    letter-spacing: 0.4px;
  }

  .name-tag {
    position: absolute;
    left: 0; top: 108px;
    width: 176px; height: 46px;
    background: linear-gradient(90deg, var(--red-orange), var(--orange));
    padding: 5px 0 0 20px;
    color: var(--white);
  }
  .name-tag__name {
    font-family: "Oswald", Arial, sans-serif;
    font-size: 16px; font-weight: 500;
    text-transform: uppercase; letter-spacing: 0.6px;
    line-height: 1.2;
  }
  .name-tag__role { font-size: 10px; line-height: 1.3; }

  .contacts {
    position: absolute;
    left: 22px; top: 166px;
    list-style: none;
  }
  .contacts__item {
    display: flex; align-items: center; gap: 8px;
    font-size: 10.5px; color: var(--text-dark);
    height: 17px;
  }
  .contacts__icon { width: 12px; height: 12px; flex: none; }
</style>
</head>
<body>

  <section class="card card--front" aria-label="Card front">
    <svg class="card__art" viewBox="0 0 520 297" preserveAspectRatio="none" aria-hidden="true">
      <defs>
        <radialGradient id="frontDark" cx="40%" cy="35%" r="75%">
          <stop offset="0" stop-color="#262626"/>
          <stop offset="1" stop-color="#050505"/>
        </radialGradient>
        <linearGradient id="frontOrange" x1="0" y1="1" x2="1" y2="0">
          <stop offset="0" stop-color="#e8381b"/>
          <stop offset="0.6" stop-color="#f7941d"/>
          <stop offset="1" stop-color="#f26522"/>
        </linearGradient>
        <linearGradient id="frontSilver" x1="0" y1="0" x2="1" y2="0">
          <stop offset="0" stop-color="#555"/>
          <stop offset="0.7" stop-color="#d8d8d8"/>
          <stop offset="1" stop-color="#8a8a8a"/>
        </linearGradient>
      </defs>
      <rect width="520" height="297" fill="url(#frontDark)"/>
      <path d="M0 222 C160 250 360 205 520 88 L520 108 C360 222 160 262 0 236 Z" fill="url(#frontSilver)"/>
      <path d="M0 238 C170 268 380 226 520 114 L520 297 L0 297 Z" fill="url(#frontOrange)"/>
      <path d="M0 240 C170 270 380 228 520 116" fill="none" stroke="#b3200f" stroke-width="1.5"/>
    </svg>
    <div class="brand">
      <span class="brand__ring"></span>
      <div class="brand__text">
        <span class="brand__name">Stride Coaching Institute</span>
        <span class="brand__tagline">Train to teach excellence</span>
      </div>
    </div>
    <p class="website">www.stridecoach.com</p>
  </section>

  <section class="card card--back" aria-label="Card back">
    <svg class="card__art" viewBox="0 0 520 297" preserveAspectRatio="none" aria-hidden="true">
      <defs>
        <linearGradient id="backPaper" x1="0" y1="0" x2="1" y2="1">
          <stop offset="0" stop-color="#ffffff"/>
          <stop offset="1" stop-color="#e4e4e4"/>
        </linearGradient>
        <linearGradient id="backOrange" x1="0" y1="1" x2="1" y2="0">
          <stop offset="0" stop-color="#e8381b"/>
          <stop offset="0.55" stop-color="#f7941d"/>
          <stop offset="1" stop-color="#e8381b"/>
        </linearGradient>
      </defs>
      <rect width="520" height="297" fill="url(#backPaper)"/>
      <path d="M150 250 C300 230 430 170 520 110 L520 128 C430 190 300 246 150 256 Z" fill="#c9c9c9"/>
      <path d="M0 264 C190 262 380 210 520 126 L520 297 L0 297 Z" fill="url(#backOrange)"/>
      <path d="M140 258 C300 246 420 190 520 130" fill="none" stroke="#ffffff" stroke-width="2" opacity="0.8"/>
    </svg>

    <div class="brand">
      <span class="brand__ring"></span>
      <div class="brand__text">
        <span class="brand__name">Stride Coaching Institute</span>
        <span class="brand__tagline">Train to teach excellence</span>
      </div>
    </div>

    <div class="name-tag">
      <p class="name-tag__name">Daniel Mercer</p>
      <p class="name-tag__role">Managing Director</p>
    </div>

    <ul class="contacts">
      <li class="contacts__item">
        <svg class="contacts__icon" viewBox="0 0 12 12" aria-hidden="true"><circle cx="6" cy="6" r="6" fill="var(--red-orange)"/><rect x="4.2" y="2.5" width="3.6" height="7" rx="0.8" fill="#fff"/></svg>
        020 555 0143
      </li>
      <li class="contacts__item">
        <svg class="contacts__icon" viewBox="0 0 12 12" aria-hidden="true"><circle cx="6" cy="6" r="6" fill="var(--red-orange)"/><path d="M3.5 3 L5 3 L5.6 4.6 L4.8 5.3 C5.3 6.3 5.8 6.8 6.7 7.2 L7.4 6.4 L9 7 L9 8.5 C6 8.8 3.2 6 3.5 3 Z" fill="#fff"/></svg>
        020 555 0178
      </li>
      <li class="contacts__item">
        <svg class="contacts__icon" viewBox="0 0 12 12" aria-hidden="true"><circle cx="6" cy="6" r="6" fill="var(--red-orange)"/><rect x="2.8" y="3.8" width="6.4" height="4.4" fill="#fff"/><path d="M2.8 3.8 L6 6.4 L9.2 3.8" fill="none" stroke="var(--red-orange)" stroke-width="0.7"/></svg>
        hello@stridecoach.com
      </li>
      <li class="contacts__item">
        <svg class="contacts__icon" viewBox="0 0 12 12" aria-hidden="true"><circle cx="6" cy="6" r="6" fill="var(--red-orange)"/><circle cx="6" cy="6" r="3.2" fill="none" stroke="#fff" stroke-width="0.8"/><path d="M2.8 6 H9.2 M6 2.8 V9.2" stroke="#fff" stroke-width="0.7"/></svg>
        www.stridecoach.com
      </li>
      <li class="contacts__item">
        <svg class="contacts__icon" viewBox="0 0 12 12" aria-hidden="true"><circle cx="6" cy="6" r="6" fill="var(--red-orange)"/><path d="M6 2.4 C4.4 2.4 3.4 3.5 3.4 4.9 C3.4 6.7 6 9.6 6 9.6 C6 9.6 8.6 6.7 8.6 4.9 C8.6 3.5 7.6 2.4 6 2.4 Z" fill="#fff"/><circle cx="6" cy="4.9" r="0.9" fill="var(--red-orange)"/></svg>
        41 Harbour Lane, Level 3, Eastfield
      </li>
    </ul>

    <p class="website">www.stridecoach.com</p>
  </section>

</body>
</html>
```